Letterhead Design Project

We are looking for a simple letterhead design that reflects our core purpose. We help our clients gain clarity and focus but we are there to help them execute. The letterhead design would mainly be utilised for engagement letters and contracts.

Target Market(s)

The customers of our business are large corporate organisations.

Requirements
Must have
• The letterhead must have the company logo
The font used must tie in to the font used in the company logo

Must have the following business details
Address: Level 10, 27 Harlow Lane, Melbourne, Australia, 3000
Phone: +61 3 527 948 183
Fax: +61 3 9042 5317
Website: www.bovrin-u.com.au
Twiiter: @bovrin_u

```html
<!DOCTYPE html>
<html lang="en">
<head>
<meta charset="utf-8">
<title>Bovrin-u Letterhead</title>
<link rel="stylesheet" href="https://fonts.googleapis.com/css2?family=Open+Sans:wght@400;600&display=swap">
<style>
  :root {
    --backdrop: #1c1c1c;
    --paper: #ffffff;
    --brand-blue: #1f5aa6;
    --brand-blue-deep: #174a8f;
    --accent-lime: #dcef3c;
    --ink-dark: #1d2b3f;
    --ink-light: #ffffff;
  }
  html, body {
    margin: 0;
    padding: 0;
    width: 1200px;
    height: 900px;
    overflow: hidden;
    background: var(--backdrop);
    font-family: "Open Sans", Arial, sans-serif;
  }
  .letterhead {
    position: absolute;
    left: 296px;
    top: 20px;
    width: 608px;
    height: 860px;
    background: var(--paper);
    overflow: hidden;
  }
  .letterhead__shapes {
    position: absolute;
    inset: 0;
    width: 608px;
    height: 860px;
  }
  .band-main { fill: var(--brand-blue); }
  .band-accent { fill: var(--accent-lime); }
  .brand-name {
    position: absolute;
    left: 20px;
    top: 16px;
    margin: 0;
    font-size: 27px;
    font-weight: 400;
    letter-spacing: 0.5px;
    color: var(--ink-light);
    line-height: 1;
  }
  .contact-block {
    position: absolute;
    right: 14px;
    top: 17px;
    text-align: right;
    color: var(--ink-dark);
    font-size: 8px;
    line-height: 12px;
  }
  .contact-block p { margin: 0; }
  .contact-block .phones span + span { margin-left: 12px; }
  .online-block {
    position: absolute;
    left: 16px;
    bottom: 14px;
    color: var(--ink-light);
    font-size: 11px;
    line-height: 15px;
  }
  .online-block p { margin: 0; }
</style>
</head>
<body>
  <main class="letterhead">
    <svg class="letterhead__shapes" viewBox="0 0 608 860" aria-hidden="true">
      <path class="band-accent" d="M300 0 H608 V28 H300 Z"/>
      <path class="band-main" d="M0 0 H608 V16 H345 C315 16 312 60 280 60 H0 Z"/>
      <path class="band-main" d="M0 860 V798 H150 C178 798 176 842 205 842 H608 V860 Z"/>
    </svg>

    <h1 class="brand-name">Bovrin-u</h1>

    <address class="contact-block">
      <p>Level 10, 27 Harlow Lane, Melbourne, Australia, 3000</p>
      <p class="phones"><span>Phone: +61 3 527 948 183</span><span>Fax: +61 3 9042 5317</span></p>
    </address>

    <div class="online-block">
      <p>Web: www.bovrin-u.com.au</p>
      <p>Twitter: @bovrin_u</p>
    </div>
  </main>
</body>
</html>
```